Defense Attorney Business Card Design Project/ Stationary

I am looking for a distinctive business card design for my solo law practice.
I practice criminal defense, both juvenile and adult, including DUI. I am a very experienced attorney with prior military experience. The design should convey a traditional, old school flair, but not be too stodgy or uptight. Some color. My logo should appear.
Updates

Project Deadline Extended Reason: I misunderstood how this project works and I was not prepared with my logo when this project ran the first time. Added Thursday, November 13, 2014

Project Deadline Extended
Reason: I was sent overseas on military duty last year, which interrupted this project. Thank you for your participation... I hope we can get this done this week! Thank you, Ben

Target Market(s)

Regular everyday people looking for strong, knowledgeable, authoritative representation while they are faced with criminal charges. Many have never been charged with a crime before. A reassuring air is therefore desired.

Industry/Entity Type

Business

Contact Information for Business Card

My information is:
Benedict L. Morrow, Attorney at Law
735 Linden Avenue Suite 400
Oakland, California 94612
Tel: (510) 555-0183
Fax: (510) 555-0147
email: benmorrowlaw@examplemail.test
web: www.benmorrowlaw.test

Font styles to use
Serif
Sans Serif
Decorative

Colors
0255a3
ffffff

Requirements
Must have
• Sharp lines, bold elements. Conservative use of colors, such as deep blues, burgundy, grays for example.
• While my logo says "Ben Morrow", it should be modified to show "Benedict L. Morrow".
Should not have
• Cliche imagery such as scales of justice, gavels, Statue of Liberty, etc.

```html
<!DOCTYPE html>
<html lang="en">
<head>
<meta charset="utf-8">
<title>Ben Morrow — Business Cards</title>
<link rel="stylesheet" href="https://fonts.googleapis.com/css2?family=Cinzel:wght@400;500&family=Raleway:wght@300;400&display=swap">
<style>
  :root {
    --backdrop: #eeeeec;
    --card-sand: #d7cfae;
    --card-navy: #1d3350;
    --ink-navy: #1d3350;
    --ink-dark: #2a2a2a;
    --cream: #e8dfc0;
    --serif: "Cinzel", "Times New Roman", serif;
    --sans: "Raleway", "Helvetica Neue", Arial, sans-serif;
  }
  * { box-sizing: border-box; margin: 0; padding: 0; }
  html, body {
    width: 1200px; height: 696px; overflow: hidden;
    background: var(--backdrop);
  }
  .canvas { position: relative; width: 1200px; height: 696px; }

  .card { position: absolute; box-shadow: 0 2px 6px rgba(0,0,0,.12); }

  /* Contact side */
  .card-contact {
    left: 110px; top: 80px; width: 320px; height: 540px;
    background: var(--card-sand);
    padding: 52px 38px 0 42px;
    color: var(--ink-dark);
  }
  .brand-small {
    display: flex; align-items: center; justify-content: center; gap: 8px;
    margin-bottom: 34px;
  }
  .brand-small .brand-mark { width: 10px; height: 10px; background: var(--ink-navy); border-radius: 50%; }
  .brand-small .brand-name {
    font-family: var(--serif); font-weight: 500; font-size: 19px;
    color: var(--ink-navy); letter-spacing: .5px;
  }
  .divider { width: 24px; height: 2px; background: var(--ink-navy); margin: 0 0 16px; }
  .section { margin-bottom: 26px; }
  .person-name {
    font-family: var(--serif); font-size: 15px; letter-spacing: .6px; margin-bottom: 4px;
  }
  .person-title { font-family: var(--sans); font-size: 13px; font-weight: 400; }
  .contact-list { list-style: none; font-family: var(--sans); font-size: 13px; line-height: 1.5; }
  .address { font-family: var(--serif); font-size: 14px; line-height: 1.5; letter-spacing: .4px; }

  /* Brand side */
  .card-brand {
    left: 610px; top: 200px; width: 520px; height: 296px;
    background: var(--card-navy);
    color: var(--cream);
  }
  .brand-large {
    position: absolute; left: 0; right: 0; top: 96px;
    display: flex; align-items: center; justify-content: center; gap: 14px;
  }
  .brand-large .brand-mark { width: 16px; height: 16px; background: var(--cream); border-radius: 50%; }
  .brand-large .brand-name {
    font-family: var(--serif); font-weight: 500; font-size: 38px; letter-spacing: 1px;
  }
  .card-brand .divider { position: absolute; left: 160px; top: 214px; background: var(--cream); }
  .web-address {
    position: absolute; left: 160px; top: 232px;
    font-family: var(--sans); font-weight: 300; font-size: 15px; letter-spacing: .3px;
  }
</style>
</head>
<body>
<main class="canvas">
  <section class="card card-contact">
    <div class="brand-small">
      <span class="brand-mark"></span>
      <span class="brand-name">Ben Morrow</span>
    </div>
    <div class="divider"></div>
    <div class="section">
      <p class="person-name">Benedict L. Morrow</p>
      <p class="person-title">Attorney at Law (Criminal Defense)</p>
    </div>
    <div class="divider"></div>
    <ul class="section contact-list">
      <li>T: (510) 555-0183</li>
      <li>F: (510) 555-0147</li>
      <li>E: benmorrowlaw@examplemail.test</li>
      <li>W: www.benmorrowlaw.test</li>
    </ul>
    <div class="divider"></div>
    <address class="address" style="font-style:normal">
      735 Linden Avenue, Suite 400<br>
      Oakland, California 94612
    </address>
  </section>

  <section class="card card-brand">
    <div class="brand-large">
      <span class="brand-mark"></span>
      <span class="brand-name">Ben Morrow</span>
    </div>
    <div class="divider"></div>
    <p class="web-address">benmorrowlaw.test</p>
  </section>
</main>
</body>
</html>
```